A poster for Natural Skincare which contains minerals and seaweed sourced from Australia

I need a poster designed for a skincare product range called Vorathique. It contains natural ingredients sourced from Australia that pack a punch!

I'd like the tag line to say Advanced Skincare Formulas Given By Nature(or any other suggestion I'll consider)

As background the range includes a vitamin C serum, a skin radiance moisturiser made from seaweed and a Mask that contains a mineral with Zeolite
It's brightening, anti ageing, protective and nourishing, results are experienced very quickly.

I have uploaded photos of the packaging for look and feel and colour but let me know if you need to see more etc.

colour of font is attached

Industry/Entity Type

Health And Wellness

Requirements
Nice to have
• could I have some designs without faces and body parts also

```html
<!DOCTYPE html>
<html lang="en">
<head>
<meta charset="utf-8">
<title>Vorathique – Advanced Skincare Formulas Given By Nature</title>
<link href="https://fonts.googleapis.com/css2?family=Cormorant+Garamond:wght@500&family=PT+Sans:wght@400;700&display=swap" rel="stylesheet">
<style>
  :root {
    --plum: #8a1846;
    --plum-dark: #6e1238;
    --leaf-dark: #3f8a25;
    --label-fill: #93d86a;
    --label-edge: #3d8a2a;
    --label-text: #1f5a1a;
    --white: #ffffff;
    --glow: #f3f7c8;
  }
  * { margin: 0; padding: 0; box-sizing: border-box; }
  html, body { width: 849px; height: 1200px; overflow: hidden; background: var(--white); }
  .poster {
    position: relative;
    width: 849px;
    height: 1200px;
    overflow: hidden;
    font-family: "PT Sans", Arial, sans-serif;
  }
  .backdrop {
    position: absolute; inset: 0;
    background:
      radial-gradient(ellipse 60% 40% at 52% 42%, var(--glow) 0%, rgba(243,247,200,0) 70%),
      linear-gradient(180deg, #4e9a2c 0%, #8cc85a 14%, #c7e79a 32%, #dff0b4 52%, #bfe28a 72%, #7cc040 86%, #4f9a22 100%);
  }
  .tagline-band {
    position: absolute; left: 0; top: 57px;
    width: 100%; height: 70px;
    background: var(--plum-dark);
    color: var(--white);
    font-size: 34px;
    line-height: 70px;
    text-align: center;
    letter-spacing: 0.3px;
  }
  .brand-title {
    position: absolute; left: 0; top: 128px;
    width: 100%;
    text-align: center;
    font-family: "Cormorant Garamond", Georgia, serif;
    font-weight: 500;
    font-size: 182px;
    line-height: 1;
    color: var(--plum);
  }
  .product-box {
    position: absolute; left: 119px; top: 560px;
    width: 192px; height: 450px;
    background: linear-gradient(90deg, #d9d9d9 0%, #ffffff 45%, #e6e6e6 100%);
    box-shadow: 4px 6px 14px rgba(0,0,0,0.18);
  }
  .origin-arc {
    position: absolute; left: 0; top: 0;
    width: 849px; height: 1200px;
    pointer-events: none;
  }
  .origin-arc text {
    font-family: "PT Sans", Arial, sans-serif;
    font-weight: 700;
    font-size: 21px;
    fill: var(--leaf-dark);
  }
  .ingredients {
    position: absolute; left: 470px; top: 440px;
    width: 360px;
    text-align: center;
    color: var(--plum);
    font-size: 28px;
    line-height: 36px;
    text-transform: uppercase;
  }
  .benefit-label {
    position: absolute; left: 410px; top: 572px;
    width: 395px; height: 228px;
  }
  .benefit-label svg { position: absolute; inset: 0; }
  .benefit-list {
    position: absolute; inset: 0;
    display: flex; flex-direction: column; justify-content: center; align-items: center;
    list-style: none;
    color: var(--label-text);
    font-size: 33px;
    line-height: 46px;
  }
  .promise {
    position: absolute; left: 330px; top: 818px;
    width: 500px;
    text-align: center;
    white-space: nowrap;
    color: var(--plum);
    font-size: 30px;
  }
</style>
</head>
<body>
<main class="poster">
  <div class="backdrop" role="img" aria-label="Photo of sunlit green leaves at the top, soft green bokeh light in the middle and fresh grass along the bottom"></div>

  <header class="tagline-band">Advanced Skincare Formulas Given By Nature</header>

  <h1 class="brand-title">Vorathique</h1>

  <div class="product-box" role="img" aria-label="Product photo of the tall white Vorathique skin radiance box"></div>

  <svg class="origin-arc" viewBox="0 0 849 1200" aria-label="Natural ingredients sourced from Australia">
    <defs>
      <path id="originCurve" d="M 25 700 C 60 440, 300 420, 470 560"/>
    </defs>
    <text><textPath href="#originCurve" textLength="575" lengthAdjust="spacing">NATURAL INGREDIENTS SOURCED FROM AUSTRALIA</textPath></text>
  </svg>

  <div class="ingredients">
    <p>Vitamin C</p>
    <p>Seaweed</p>
    <p>Mineral with Zeolite</p>
  </div>

  <div class="benefit-label">
    <svg viewBox="0 0 395 228" width="395" height="228" aria-hidden="true">
      <path d="M 40 4 H 355 Q 358 30 391 34 V 194 Q 358 198 355 224 H 40 Q 37 198 4 194 V 34 Q 37 30 40 4 Z"
            fill="var(--label-fill)" stroke="var(--label-edge)" stroke-width="3"/>
      <path d="M 48 14 H 347 Q 352 38 381 42 V 186 Q 352 190 347 214 H 48 Q 43 190 14 186 V 42 Q 43 38 48 14 Z"
            fill="none" stroke="var(--label-edge)" stroke-width="2" stroke-dasharray="3 5"/>
    </svg>
    <ul class="benefit-list">
      <li>brightening</li>
      <li>anti ageing</li>
      <li>protective</li>
      <li>nourishing</li>
    </ul>
  </div>

  <p class="promise">results are experienced very quickly</p>
</main>
</body>
</html>
```